Diagramm/Grafik zur Darstellung einer Formel
Zielgruppe
Das Unternehmen ist in der Unternehmensberatung tätig und beschäftigt sich mit der Analyse von IT-In- und Outsourcing.
Zielgruppe: Entscheider / Höheres Management / Round Table
Aufgabenstellung
Es wurde für die Bewertung des bestehenden Outsourcing eine Formel entwickelt, welche es ermöglicht einerseits die Stärken
und Schwächen und andererseits die Entwicklung und Vorteilhaftigkeit der Kosten für die nächsten Jahre zu prognostizieren.
Der Name der Formel ist "MIRAX-P Methode" (Strategie, Technologie, Organisation, Qualität und Kosten)
Die Formel ist aufgebaut aus 5 Sektoren, unter welchem jeweils 3-8 Faktoren untergeordnet sind. (siehe IMG_1159)
Die Zuordnung der Faktoren zu Sektoren (siehe SektorenFaktoren.pdf) ist variabel, aus welchem Grund unter jedem Sektor 3-8 Faktoren unterordnenbar sein sollten.
Grundsätzlich findet die Auswertung aus dem Vergleich von Kosten + Risiken - Chancen jeweils von Outsourcing und Insourcing statt. (siehe IMG_1190)
Ziel ist es, eine Darstellung der Sektoren und Faktoren sowie der Formel zu finden, welche:
a) die Abhängigkeit von den Faktoren zu den Sektoren darstellt
b) die Formel darstellt
c) sich als Ganzes oder in Teilen für diverse Unterlagen verwenden lässt (bspw. .pptx, .pdf, etc.)
--> es ist geplant diese Darstellung bspw. als Ganzes oder in Teilen in eine PowerPoint-Präsentation zu integrieren
Diese Aufgabenstellung ist ein erster Versuch mittels der Plattform pixelhafen.de Aufträge zu vergeben.
Bei Erfolg sind Anschlussaufträge geplant.
WICHTIG: Alle Anhänge diesen lediglich zur Darstellung der Zusammenhänge, sollen aber keinerlei design vorgeben!

```html
<!DOCTYPE html>
<html lang="de">
<head>
<meta charset="utf-8">
<title>MIRAX-P Methode</title>
<link href="https://fonts.googleapis.com/css2?family=Barlow:wght@400;500;600;700&display=swap" rel="stylesheet">
<style>
  :root {
    --band: #56789b;
    --orange: #e2570f;
    --text-grey: #666a6e;
    --panel-blue: #8ea8be;
    --panel-grey: #efefef;
    --dot-blue: #7d9dbb;
    --brace-blue: #8ea8be;
    --white: #ffffff;
    --bullet: #d9d9d9;
    --bullet-dark: #7d9dbb;
  }
  * { box-sizing: border-box; margin: 0; padding: 0; }
  html, body { width: 1200px; height: 900px; overflow: hidden; background: var(--white); }
  body { font-family: "Barlow", Arial, sans-serif; position: relative; }

  .header-band {
    position: absolute; left: 0; top: 0; width: 1200px; height: 66px;
    background: var(--band); display: flex; align-items: center; justify-content: center;
  }
  .method-title {
    color: var(--white); font-weight: 700; font-size: 40px; letter-spacing: 9px;
  }
  .footer-band { position: absolute; left: 0; bottom: 0; width: 1200px; height: 15px; background: var(--band); }

  .divider { position: absolute; left: 585px; top: 70px; width: 30px; height: 760px; }
  .compare-sign { position: absolute; left: 573px; top: 232px; width: 54px; height: 92px; }

  .side-title {
    position: absolute; top: 106px; width: 420px; text-align: center;
    color: var(--orange); font-weight: 700; font-size: 33px; letter-spacing: 5px;
  }
  .brace-top { position: absolute; top: 150px; width: 390px; height: 70px; }
  .formula {
    position: absolute; top: 234px; color: var(--text-grey);
    font-weight: 600; font-size: 30px; letter-spacing: 3.6px; white-space: nowrap;
  }
  .formula .paren { color: var(--orange); }
  .brace-sub { position: absolute; top: 285px; width: 282px; height: 46px; }
  .dot-arrow { position: absolute; width: 20px; }

  .panel-costs { position: absolute; top: 456px; height: 179px; background: var(--panel-grey); padding: 20px 0 0 14px; }
  .panel-factors {
    position: absolute; top: 456px; height: 362px; background: var(--panel-blue);
    display: grid; grid-template-columns: 1fr 1fr; padding: 18px 0 0 26px; row-gap: 14px;
  }
  .sector-name {
    display: flex; align-items: center; gap: 6px;
    font-size: 13px; font-weight: 600; color: var(--white); text-transform: uppercase; height: 22px;
  }
  .panel-costs .sector-name { color: #555; }
  .sector-name::before {
    content: ""; width: 21px; height: 21px; border-radius: 50%; background: var(--bullet); flex: none;
  }
  .panel-costs .sector-name::before { background: var(--bullet-dark); }
  .factor-list { list-style: none; padding-left: 27px; margin-top: 1px; }
  .factor-list li { font-size: 12px; line-height: 16.3px; color: var(--white); }
  .panel-costs .factor-list li { color: #555; }

  .footnote {
    position: absolute; top: 847px; width: 1200px; text-align: center;
    color: var(--orange); font-size: 21px; font-weight: 500;
  }
</style>
</head>
<body>
  <header class="header-band"><h1 class="method-title">MIRAX-P</h1></header>

  <svg class="divider" viewBox="0 0 30 760">
    <line x1="15" y1="0" x2="15" y2="750" stroke="var(--dot-blue)" stroke-width="4" stroke-linecap="round" stroke-dasharray="0.1 10"/>
    <polyline points="6,740 15,750 24,740" fill="none" stroke="var(--dot-blue)" stroke-width="3"/>
  </svg>
  <svg class="compare-sign" viewBox="0 0 54 92">
    <rect x="2" y="2" width="50" height="88" fill="var(--white)" stroke="var(--dot-blue)" stroke-width="4" stroke-dasharray="0.1 8" stroke-linecap="round"/>
    <g stroke="var(--dot-blue)" stroke-width="3" fill="none">
      <polyline points="13,22 27,34 41,22"/>
      <line x1="13" y1="40" x2="41" y2="40"/>
      <line x1="13" y1="52" x2="41" y2="52"/>
      <polyline points="13,70 27,58 41,70"/>
    </g>
  </svg>

  <!-- Outsourcing -->
  <section class="side side-out">
    <h2 class="side-title" style="left:87px">OUTSOURCING*</h2>
    <svg class="brace-top" style="left:102px" viewBox="0 0 390 70">
      <path d="M3,68 C3,32 12,27 42,27 H165 C185,27 195,17 195,3 C195,17 205,27 225,27 H348 C378,27 387,32 387,68" fill="none" stroke="var(--orange)" stroke-width="5"/>
    </svg>
    <p class="formula" style="left:75px">OS + <span class="paren">(</span>Chancen - Risiken<span class="paren">)</span></p>
    <svg class="brace-sub" style="left:214px" viewBox="0 0 282 46">
      <path d="M2,0 C2,18 10,22 32,22 H122 C136,22 141,30 141,44 C141,30 146,22 160,22 H250 C272,22 280,18 280,0" fill="none" stroke="var(--brace-blue)" stroke-width="4"/>
    </svg>
    <svg class="dot-arrow" style="left:102px;top:288px;height:116px" viewBox="0 0 20 116">
      <line x1="10" y1="2" x2="10" y2="106" stroke="var(--dot-blue)" stroke-width="4" stroke-linecap="round" stroke-dasharray="0.1 10"/>
      <polyline points="2,104 10,113 18,104" fill="none" stroke="var(--dot-blue)" stroke-width="3"/>
    </svg>
    <svg class="dot-arrow" style="left:345px;top:332px;height:72px" viewBox="0 0 20 72">
      <line x1="10" y1="2" x2="10" y2="62" stroke="var(--dot-blue)" stroke-width="4" stroke-linecap="round" stroke-dasharray="0.1 10"/>
      <polyline points="2,60 10,69 18,60" fill="none" stroke="var(--dot-blue)" stroke-width="3"/>
    </svg>

    <div class="panel-costs" style="left:21px;width:174px">
      <div class="sector"><h3 class="sector-name">Kosten</h3>
        <ol class="factor-list"><li>1.</li><li>2.</li><li>3.</li><li>4.</li><li>5.</li><li>6.</li><li>7.</li><li>8.</li></ol></div>
    </div>
    <div class="panel-factors" style="left:210px;width:312px">
      <div class="sector"><h3 class="sector-name">Strategie</h3>
        <ol class="factor-list"><li>1.</li><li>2.</li><li>3.</li><li>4.</li><li>5.</li><li>6.</li><li>7.</li><li>8.</li></ol></div>
      <div class="sector"><h3 class="sector-name">Technologie</h3>
        <ol class="factor-list"><li>1.</li><li>2.</li><li>3.</li><li>4.</li><li>5.</li><li>6.</li><li>7.</li><li>8.</li></ol></div>
      <div class="sector"><h3 class="sector-name">Organisation</h3>
        <ol class="factor-list"><li>1.</li><li>2.</li><li>3.</li><li>4.</li><li>5.</li><li>6.</li><li>7.</li><li>8.</li></ol></div>
      <div class="sector"><h3 class="sector-name">Qualität</h3>
        <ol class="factor-list"><li>1.</li><li>2.</li><li>3.</li><li>4.</li><li>5.</li><li>6.</li><li>7.</li><li>8.</li></ol></div>
    </div>
  </section>

  <!-- Insourcing -->
  <section class="side side-in">
    <h2 class="side-title" style="left:710px">INSOURCING*</h2>
    <svg class="brace-top" style="left:714px" viewBox="0 0 390 70">
      <path d="M3,68 C3,32 12,27 42,27 H165 C185,27 195,17 195,3 C195,17 205,27 225,27 H348 C378,27 387,32 387,68" fill="none" stroke="var(--orange)" stroke-width="5"/>
    </svg>
    <p class="formula" style="left:690px">IS + <span class="paren">(</span>Chancen - Risiken<span class="paren">)</span></p>
    <svg class="brace-sub" style="left:810px" viewBox="0 0 282 46">
      <path d="M2,0 C2,18 10,22 32,22 H122 C136,22 141,30 141,44 C141,30 146,22 160,22 H250 C272,22 280,18 280,0" fill="none" stroke="var(--brace-blue)" stroke-width="4"/>
    </svg>
    <svg class="dot-arrow" style="left:689px;top:288px;height:116px" viewBox="0 0 20 116">
      <line x1="10" y1="2" x2="10" y2="106" stroke="var(--dot-blue)" stroke-width="4" stroke-linecap="round" stroke-dasharray="0.1 10"/>
      <polyline points="2,104 10,113 18,104" fill="none" stroke="var(--dot-blue)" stroke-width="3"/>
    </svg>
    <svg class="dot-arrow" style="left:941px;top:332px;height:72px" viewBox="0 0 20 72">
      <line x1="10" y1="2" x2="10" y2="62" stroke="var(--dot-blue)" stroke-width="4" stroke-linecap="round" stroke-dasharray="0.1 10"/>
      <polyline points="2,60 10,69 18,60" fill="none" stroke="var(--dot-blue)" stroke-width="3"/>
    </svg>

    <div class="panel-costs" style="left:632px;width:178px">
      <div class="sector"><h3 class="sector-name">Kosten</h3>
        <ol class="factor-list"><li>1.</li><li>2.</li><li>3.</li><li>4.</li><li>5.</li><li>6.</li><li>7.</li><li>8.</li></ol></div>
    </div>
    <div class="panel-factors" style="left:822px;width:300px">
      <div class="sector"><h3 class="sector-name">Strategie</h3>
        <ol class="factor-list"><li>1.</li><li>2.</li><li>3.</li><li>4.</li><li>5.</li><li>6.</li><li>7.</li><li>8.</li></ol></div>
      <div class="sector"><h3 class="sector-name">Technologie</h3>
        <ol class="factor-list"><li>1.</li><li>2.</li><li>3.</li><li>4.</li><li>5.</li><li>6.</li><li>7.</li><li>8.</li></ol></div>
      <div class="sector"><h3 class="sector-name">Organisation</h3>
        <ol class="factor-list"><li>1.</li><li>2.</li><li>3.</li><li>4.</li><li>5.</li><li>6.</li><li>7.</li><li>8.</li></ol></div>
      <div class="sector"><h3 class="sector-name">Qualität</h3>
        <ol class="factor-list"><li>1.</li><li>2.</li><li>3.</li><li>4.</li><li>5.</li><li>6.</li><li>7.</li><li>8.</li></ol></div>
    </div>
  </section>

  <p class="footnote">*Vergleich der Nutzen v. Is / Os</p>
  <div class="footer-band"></div>
</body>
</html>
```